Game, Voice & Dedicated Server Company Needs a Business Card Design

We need a new business card design, centered around our new logo (PSD provided below).

Designs that we do like:
https://pixelmarsh.net/item/corporate-business-card/5382017?s_rank=43 (needs to be made more eye catching)

Our main areas of business are:
- Dedicated Servers
- Game Servers
- Voice Servers
- Mitigation Security Specialists

Industry/Entity Type

Business

Contact Information for Business Card

On the card: (and anything else you would suggest)
- Staff member name
- Staff member position in company
- Staff member phone number
- Staff member email
- Other / Staff member Skype
- Website link

Colors
9bcb3c
abd036

Requirements
Must have
• Design of Card:
• - Green (same green as the logo)
• - Business / Corporate design
• - Something a little different / abstract that shouts premium

```html
<!DOCTYPE html>
<html lang="en">
<head>
<meta charset="utf-8">
<title>Brightpath Hosting – Business Card</title>
<link rel="stylesheet" href="https://fonts.googleapis.com/css2?family=Montserrat:wght@400;500;700&display=swap">
<style>
  :root {
    --backdrop: #2a2a2c;
    --card: #ffffff;
    --green: #8cc63f;
    --grey-dark: #58595b;
    --grey-mid: #808285;
    --grey-light: #a7a9ac;
  }
  * { box-sizing: border-box; margin: 0; padding: 0; }
  html, body { width: 1200px; height: 900px; overflow: hidden; }
  body {
    background: var(--backdrop);
    font-family: "Montserrat", Arial, sans-serif;
    position: relative;
  }
  .card {
    position: absolute;
    left: 285px;
    width: 630px;
    height: 360px;
    background: var(--card);
    border-radius: 22px;
    overflow: hidden;
  }
  .card--front { top: 70px; }
  .card--back { top: 470px; }

  /* Front */
  .brand-mark {
    position: absolute;
    display: flex;
    align-items: center;
    gap: 14px;
  }
  .brand-mark__dot {
    width: 26px; height: 26px;
    border-radius: 50%;
    background: var(--green);
    flex: none;
  }
  .brand-mark__name {
    font-weight: 700;
    color: var(--green);
    text-transform: uppercase;
    line-height: 1.05;
  }
  .card--front .brand-mark { top: 70px; right: 60px; }
  .card--front .brand-mark__name { font-size: 34px; }

  .services {
    position: absolute;
    left: 48px;
    bottom: 44px;
    font-size: 15px;
    line-height: 1.45;
    color: var(--grey-mid);
    letter-spacing: 0.2px;
  }
  .services .accent { color: var(--green); }

  /* Back */
  .card--back .brand-mark { top: 56px; left: 44px; gap: 12px; }
  .card--back .brand-mark__dot { width: 22px; height: 22px; border-radius: 3px; }
  .card--back .brand-mark__name { font-size: 26px; }

  .contact {
    position: absolute;
    right: 48px;
    top: 150px;
    width: 280px;
  }
  .contact__name {
    font-size: 28px;
    font-weight: 700;
    color: var(--green);
    letter-spacing: 0.4px;
  }
  .contact__role {
    font-size: 14px;
    color: var(--grey-mid);
    margin: 2px 0 14px;
  }
  .contact__list { list-style: none; }
  .contact__item {
    display: flex;
    align-items: center;
    gap: 10px;
    font-size: 14.5px;
    color: var(--grey-mid);
    line-height: 1.6;
  }
  .contact__icon { width: 12px; height: 12px; flex: none; }
</style>
</head>
<body>

  <section class="card card--front" aria-label="Card front">
    <div class="brand-mark">
      <span class="brand-mark__dot"></span>
      <span class="brand-mark__name">Brightpath<br>Hosting</span>
    </div>
    <div class="services">
      <p>Dedicated Servers <span class="accent">-</span> Game Servers</p>
      <p>Voice Servers <span class="accent">-</span> Business relations</p>
      <p>www.<span class="accent">brightpathhosting</span>.com</p>
    </div>
  </section>

  <section class="card card--back" aria-label="Card back">
    <div class="brand-mark">
      <span class="brand-mark__dot"></span>
      <span class="brand-mark__name">Brightpath<br>Hosting</span>
    </div>

    <div class="contact">
      <h1 class="contact__name">Marek Olsen</h1>
      <p class="contact__role">Director</p>
      <ul class="contact__list">
        <li class="contact__item">
          <svg class="contact__icon" viewBox="0 0 12 12"><path d="M2.5 1 L4.5 1 L5.3 3.5 L4 4.5 Q5 7 7.5 8 L8.5 6.7 L11 7.5 L11 9.5 Q10.5 11 9 11 Q1 10 1 3 Q1 1.5 2.5 1 Z" fill="var(--green)"/></svg>
          +330 2518-4096
        </li>
        <li class="contact__item">
          <svg class="contact__icon" viewBox="0 0 12 12"><rect x="0.8" y="2.3" width="10.4" height="7.4" rx="1" fill="none" stroke="var(--green)" stroke-width="1.4"/><path d="M1 2.8 L6 6.5 L11 2.8" fill="none" stroke="var(--green)" stroke-width="1.4"/></svg>
          info@brightpathhosting.com
        </li>
        <li class="contact__item">
          <svg class="contact__icon" viewBox="0 0 12 12"><circle cx="6" cy="6" r="5" fill="var(--green)"/></svg>
          @brightpathhosting.com
        </li>
        <li class="contact__item">
          <svg class="contact__icon" viewBox="0 0 12 12"><circle cx="6" cy="6" r="5" fill="none" stroke="var(--green)" stroke-width="1.3"/><ellipse cx="6" cy="6" rx="2.2" ry="5" fill="none" stroke="var(--green)" stroke-width="1.1"/><path d="M1 6 H11" stroke="var(--green)" stroke-width="1.1"/></svg>
          www.brightpathhosting.com
        </li>
      </ul>
    </div>
  </section>

</body>
</html>
```